Webbanner-Design für Beteiligungsunternehmen
Zielgruppe
Ich habe ein kleines Familieninternes Beteiligungsunternehmen welches an verschiedenen Firmen beteiligt ist.
Aufgabenstellung
Ich brauche ein Profilbanner für Facebook und Twitter welches zum einen meine Hauptmarke 'Trelvik Holding' und meine Unternehmen an denen ich beteiligt bin (Geldwunder/Kalindor Real Estate/ TB Holding/Murelto) zeigt.

```html
<!DOCTYPE html>
<html lang="de">
<head>
<meta charset="utf-8">
<title>Trelvik Holding – Profilbanner</title>
<link href="https://fonts.googleapis.com/css2?family=Exo+2:wght@500;600&display=swap" rel="stylesheet">
<style>
  :root {
    --page-bg: #ffffff;
    --brick-dark: #5a2a26;
    --brick-mid: #7a3a31;
    --brick-warm: #9a4a36;
    --mortar: #b9ada0;
    --band: rgba(128, 118, 116, 0.88);
    --ink: #ffffff;
    --shadow: rgba(0, 0, 0, 0.35);
  }
  * { margin: 0; padding: 0; box-sizing: border-box; }
  html, body {
    width: 1200px;
    height: 845px;
    overflow: hidden;
    background: var(--page-bg);
  }
  .canvas {
    position: relative;
    width: 1200px;
    height: 845px;
  }
  .banner {
    position: absolute;
    overflow: hidden;
    box-shadow: 0 4px 12px var(--shadow);
    font-family: "Exo 2", sans-serif;
    color: var(--ink);
  }
  .banner--small { left: 321px; top: 80px; width: 562px; height: 213px; --s: 0.547; }
  .banner--large { left: 88px; top: 426px; width: 1028px; height: 342px; --s: 1; }

  .banner__wall {
    position: absolute;
    inset: 0;
    background:
      radial-gradient(ellipse at 75% 30%, rgba(170, 80, 50, 0.45), transparent 55%),
      radial-gradient(ellipse at 20% 70%, rgba(160, 75, 50, 0.35), transparent 50%),
      linear-gradient(160deg, var(--brick-mid) 0%, var(--brick-dark) 45%, var(--brick-warm) 75%, var(--brick-mid) 100%);
  }
  .banner__title {
    position: absolute;
    left: 0;
    right: 0;
    top: 41%;
    text-align: center;
    font-weight: 600;
    font-size: calc(42px * var(--s));
    letter-spacing: calc(2px * var(--s));
    text-transform: uppercase;
    line-height: 1;
  }
  .banner__partners {
    position: absolute;
    left: 0;
    right: 0;
    bottom: 0;
    height: 29%;
    background: var(--band);
  }
  .partner {
    position: absolute;
    top: 50%;
    transform: translate(-50%, -50%);
    white-space: nowrap;
    font-weight: 500;
    font-size: calc(20px * var(--s));
    letter-spacing: calc(1.5px * var(--s));
    text-transform: uppercase;
  }
  .partner--geldwunder { left: 15%; }
  .partner--kalindor { left: 38.5%; }
  .partner--tb { left: 61%; }
  .partner--murelto { left: 83%; }
</style>
</head>
<body>
<main class="canvas">
  <section class="banner banner--small">
    <div class="banner__wall" role="img" aria-label="Backsteinmauer aus roten und braunen Ziegeln"></div>
    <h1 class="banner__title">Trelvik Holding</h1>
    <div class="banner__partners">
      <span class="partner partner--geldwunder">Geldwunder</span>
      <span class="partner partner--kalindor">Kalindor Real Estate</span>
      <span class="partner partner--tb">TB Holding</span>
      <span class="partner partner--murelto">Murelto</span>
    </div>
  </section>

  <section class="banner banner--large">
    <div class="banner__wall" role="img" aria-label="Backsteinmauer aus roten und braunen Ziegeln"></div>
    <h1 class="banner__title">Trelvik Holding</h1>
    <div class="banner__partners">
      <span class="partner partner--geldwunder">Geldwunder</span>
      <span class="partner partner--kalindor">Kalindor Real Estate</span>
      <span class="partner partner--tb">TB Holding</span>
      <span class="partner partner--murelto">Murelto</span>
    </div>
  </section>
</main>
</body>
</html>
```